Little Meadow Press Website

We need a wordpress design for a new independent children's book publishers based in Oxford in the UK. The design should be fun and colourful. I have supplied an example template of some of the text/images but open to other ideas.
The design should communicate that Little Meadow Press are producers of fun and interactive children's illustrated books.

Target Market(s)

Booksellers, International

```html
<!DOCTYPE html>
<html lang="en">
<head>
<meta charset="utf-8">
<title>Contact – Little Meadow Press</title>
<link rel="stylesheet" href="https://fonts.googleapis.com/css2?family=Gochi+Hand&family=Arimo:wght@400&display=swap">
<style>
  :root {
    --sky-top: #9fd8f7;
    --sky-low: #dff2fc;
    --page: #ffffff;
    --ink: #2b2b2b;
    --blue: #2a8ac8;
    --red: #e8202a;
    --orange: #f7941d;
    --green: #8dc63f;
    --purple: #92278f;
    --navy: #2e3192;
    --grass: #c4df72;
    --paper: #eef8fc;
    --frame: #f1f1ea;
  }
  * { margin: 0; padding: 0; box-sizing: border-box; }
  html, body { width: 1122px; height: 1200px; overflow: hidden; }
  body {
    position: relative;
    background: linear-gradient(to bottom, var(--sky-top) 0, var(--sky-low) 210px, var(--page) 300px, var(--page) 100%);
    font-family: "Arimo", Arial, sans-serif;
    color: var(--ink);
  }
  .hand { font-family: "Gochi Hand", cursive; font-weight: 400; }

  .brand-banner {
    position: absolute; left: 66px; top: 6px; width: 314px; height: 140px;
    background: var(--paper);
    border-radius: 4px;
    box-shadow: 0 2px 8px rgba(80,140,180,.25);
    display: flex; align-items: center; justify-content: center; gap: 10px;
  }
  .brand-dot { width: 16px; height: 16px; border-radius: 50%; background: var(--orange); }
  .brand-name { font-size: 22px; color: var(--blue); letter-spacing: .5px; }

  .main-nav {
    position: absolute; left: 515px; top: 89px; width: 472px; height: 48px;
    background: #f2f2f2; border-radius: 4px;
    display: flex; align-items: center; justify-content: space-around;
    padding: 0 12px;
  }
  .main-nav a { text-decoration: none; font-size: 22px; }
  .nav-home { color: var(--blue); }
  .nav-about { color: var(--red); }
  .nav-books { color: var(--orange); }
  .nav-authors { color: var(--green); }
  .nav-contact { color: var(--purple); }

  .grass-strip {
    position: absolute; left: 72px; top: 166px; width: 976px; height: 28px;
    background: linear-gradient(to bottom, rgba(196,223,114,0) 0, var(--grass) 100%);
  }
  .butterfly {
    position: absolute; left: 982px; top: 138px; width: 94px; height: 86px;
    background: #f08a1e; border-radius: 40% 40% 45% 45%;
  }

  .hero-frame {
    position: absolute; left: 72px; top: 192px; width: 976px; height: 164px;
    background: var(--frame);
    box-shadow: 0 3px 4px rgba(0,0,0,.12);
  }
  .hero-photo {
    position: absolute; left: 7px; top: 17px; width: 962px; height: 116px;
    border-radius: 6px;
    background: linear-gradient(to right, #c9a9a5 0, #b7a8a6 35%, #9d8f8c 70%, #8c7f78 100%);
  }
  .hero-title {
    position: absolute; left: 0; right: 0; top: 46px; text-align: center;
    font-size: 44px; color: #fff; text-shadow: 0 1px 3px rgba(0,0,0,.3);
  }

  .contact-block { position: absolute; width: 420px; }
  .contact-block h2 { font-size: 26px; line-height: 1; margin-bottom: 14px; }
  .contact-block p { font-size: 15.5px; line-height: 21.5px; }
  .contact-block.centered { left: 361px; width: 400px; text-align: center; }

  .address { left: 84px; top: 388px; }
  .address h2 { color: var(--blue); }
  .telephone { left: 590px; top: 388px; }
  .telephone h2 { color: var(--red); }
  .enquiries { left: 84px; top: 524px; }
  .enquiries h2 { color: var(--green); }
  .publicity { left: 590px; top: 524px; }
  .publicity h2 { color: var(--purple); }
  .sales { top: 679px; }
  .sales h2 { color: var(--orange); }
  .director { top: 823px; }
  .director h2 { color: var(--navy); }

  .footer-scene {
    position: absolute; left: 0; top: 998px; width: 1122px; height: 202px;
    background: linear-gradient(to bottom, #ffffff 0, #b9ddf2 18%, #9cce5a 38%, #6ea834 52%, #a9dbf7 53%, #9fd6f6 100%);
  }
  .footer-note {
    position: absolute; left: 0; right: 0; top: 1136px; text-align: center;
    font-size: 13.5px; color: #111;
  }
</style>
</head>
<body>
  <header>
    <div class="brand-banner">
      <span class="brand-dot"></span>
      <span class="brand-name">Little Meadow Press</span>
    </div>
    <nav class="main-nav hand">
      <a class="nav-home" href="#">Home</a>
      <a class="nav-about" href="#">About</a>
      <a class="nav-books" href="#">Books</a>
      <a class="nav-authors" href="#">Authors</a>
      <a class="nav-contact" href="#">Contact</a>
    </nav>
    <div class="grass-strip" role="img" aria-label="Strip of drawn grass"></div>
    <div class="butterfly" role="img" aria-label="Orange butterfly illustration"></div>
  </header>

  <section class="hero-frame">
    <div class="hero-photo" role="img" aria-label="Photo of a child painting with red paint at a table"></div>
    <h1 class="hero-title hand">Contact</h1>
  </section>

  <main>
    <div class="contact-block address">
      <h2 class="hand">Address</h2>
      <p>Lorem Ipsum is simply dummy text of the printing and typesetting industry.</p>
    </div>
    <div class="contact-block telephone">
      <h2 class="hand">Telephone</h2>
      <p>+ 100 200 300<br>+ 400 500 6000</p>
    </div>
    <div class="contact-block enquiries">
      <h2 class="hand">General enquiries</h2>
      <p>info@littlemeadowpress.com<br>enquiry@littlemeadowpress.com</p>
    </div>
    <div class="contact-block publicity">
      <h2 class="hand">PUBLICITY and MARKETING</h2>
      <p>+ 100 200 300<br>+ 400 500 6000</p>
    </div>
    <div class="contact-block centered sales">
      <h2 class="hand">sales &amp; distribution</h2>
      <p>Lorem Ipsum is simply dummy text of the printing and typesetting industry.</p>
    </div>
    <div class="contact-block centered director">
      <h2 class="hand">MANAGING DIRECTOR</h2>
      <p>Lorem Ipsum is simply dummy text of the printing and typesetting industry.</p>
    </div>
  </main>

  <footer>
    <div class="footer-scene" role="img" aria-label="Landscape of hills, palm tree island, sailboat, rainbow and dolphins in the sea"></div>
    <p class="footer-note">© Little Meadow Press - 2015. All Rights Reserved.</p>
  </footer>
</body>
</html>
```